Tirovel

We need a business card for our company is a holding for different business all are different we try to have some air of relax and fun in our projects we add pictures of the office to give you an idea od the mood of the business

Business

```html
<!DOCTYPE html>
<html lang="en">
<head>
<meta charset="utf-8">
<title>Tirovel – Business Card</title>
<link rel="stylesheet" href="https://fonts.googleapis.com/css2?family=Montserrat:wght@300;400;700;800&display=swap">
<style>
  :root {
    --stage: #e6e6e4;
    --card-yellow: #f4e63c;
    --card-yellow-light: #f7ec62;
    --card-yellow-deep: #efdc22;
    --rule-white: #ffffff;
    --ink-brown: #5b3b17;
    --shadow: rgba(0, 0, 0, 0.18);
  }
  * { margin: 0; padding: 0; box-sizing: border-box; }
  html, body {
    width: 1200px;
    height: 777px;
    overflow: hidden;
    background: var(--stage);
    font-family: "Montserrat", sans-serif;
  }
  .stage {
    position: relative;
    width: 1200px;
    height: 777px;
    display: flex;
    align-items: center;
    justify-content: center;
  }
  .business-card {
    position: relative;
    width: 840px;
    height: 480px;
    background: var(--card-yellow);
    box-shadow: 0 14px 34px var(--shadow);
    overflow: hidden;
    color: var(--ink-brown);
  }
  .card-grid {
    position: absolute;
    inset: 0;
    width: 100%;
    height: 100%;
  }
  .brand-block {
    position: absolute;
    left: 58px;
    top: 292px;
    display: flex;
    align-items: center;
    gap: 12px;
  }
  .brand-dot {
    width: 36px;
    height: 36px;
    border-radius: 50%;
    background: var(--rule-white);
  }
  .brand-name {
    font-weight: 800;
    font-size: 44px;
    letter-spacing: -2px;
    line-height: 1;
    color: var(--ink-brown);
  }
  .person {
    position: absolute;
    left: 322px;
    top: 212px;
    display: inline-block;
    text-align: right;
  }
  .person-name {
    font-weight: 700;
    font-size: 29px;
    letter-spacing: -1px;
    line-height: 1;
    white-space: nowrap;
  }
  .person-role {
    margin-top: 6px;
    font-weight: 400;
    font-size: 13px;
  }
  .contact-top {
    position: absolute;
    left: 600px;
    top: 72px;
  }
  .phone {
    font-weight: 700;
    font-size: 29px;
    letter-spacing: -1px;
    line-height: 1;
    white-space: nowrap;
  }
  .address {
    margin-top: 10px;
    font-weight: 300;
    font-size: 15px;
    line-height: 1.4;
  }
  .contact-bottom {
    position: absolute;
    left: 588px;
    top: 360px;
  }
  .email {
    font-weight: 300;
    font-size: 15px;
  }
  .website {
    margin-top: 6px;
    font-weight: 700;
    font-size: 22px;
    letter-spacing: -0.5px;
    white-space: nowrap;
  }
</style>
</head>
<body>
<main class="stage">
  <article class="business-card">
    <svg class="card-grid" viewBox="0 0 840 480" aria-hidden="true">
      <polygon points="0,0 300,0 300,160 0,200" fill="var(--card-yellow-light)"/>
      <polygon points="300,290 565,290 565,480 300,480" fill="var(--card-yellow-deep)"/>
      <g stroke="var(--rule-white)" stroke-width="4" fill="none">
        <line x1="0" y1="200" x2="300" y2="160"/>
        <line x1="300" y1="0" x2="300" y2="480"/>
        <line x1="300" y1="290" x2="840" y2="290"/>
        <line x1="565" y1="290" x2="565" y2="480"/>
        <line x1="40" y1="200" x2="40" y2="440"/>
        <line x1="40" y1="440" x2="300" y2="440"/>
        <line x1="700" y1="0" x2="840" y2="60"/>
      </g>
    </svg>

    <div class="brand-block">
      <span class="brand-dot"></span>
      <span class="brand-name">Tirovel</span>
    </div>

    <div class="person">
      <p class="person-name">Marcus Lee Hale</p>
      <p class="person-role">CEO / Director</p>
    </div>

    <div class="contact-top">
      <p class="phone">555-204-1186</p>
      <p class="address">1450 Meadowlark Lane<br>Riverton, OR 97301</p>
    </div>

    <div class="contact-bottom">
      <p class="email">inquiry@tirovel.com</p>
      <p class="website">www.tirovel.com</p>
    </div>
  </article>
</main>
</body>
</html>
```